Business Card Design

I would like a new business card design for an accounting firm that specializes in resolving clients tax problems. I want the card to give the impression that we are not your typical stodgy accounting firm, but at the same time we will get the job done.
Industry/Entity Type
Business
Contact Information for Business Card
Dorian T Welsby
Certified Public Accountant
38-27 52nd Street
Sunnyside, NY 11287
Tel: (718) 555-0142
Fax: (888) 555-0199
e-mail: dtwthecpa@ledgerpost.com
website: harborfilingreliefexperts.com

```html
<!DOCTYPE html>
<html lang="en">
<head>
<meta charset="utf-8">
<title>Dorian T Welsby – Business Card</title>
<link rel="stylesheet" href="https://fonts.googleapis.com/css2?family=Open+Sans:wght@400;600;700&display=swap">
<style>
  :root {
    --page-bg: #e9e9e7;
    --card-bg: #fbfbfa;
    --brand-blue: #2f64ad;
    --accent-gold: #f2c230;
    --icon-blue: #2e6fc0;
    --ink-gray: #4a4a4a;
    --dot-blue: #3a72c4;
  }
  * { margin: 0; padding: 0; box-sizing: border-box; }
  html, body {
    width: 1200px; height: 1023px; overflow: hidden;
    background: var(--page-bg);
    font-family: "Open Sans", Arial, sans-serif;
  }
  .card {
    position: absolute; left: 100px; top: 226px;
    width: 1000px; height: 572px;
    background: var(--card-bg);
    border-radius: 6px;
    box-shadow: 0 6px 24px rgba(0,0,0,.18);
    overflow: hidden;
  }
  .brand {
    position: absolute; left: 64px; top: 62px;
    display: flex; align-items: center; gap: 16px;
  }
  .brand-square { width: 34px; height: 34px; border-radius: 6px; background: var(--accent-gold); }
  .brand-name {
    font-weight: 700; font-size: 30px; letter-spacing: 2px;
    color: var(--brand-blue); text-transform: uppercase;
  }
  .identity { position: absolute; left: 64px; top: 232px; }
  .identity-name { font-weight: 600; font-size: 40px; color: var(--brand-blue); line-height: 1.1; }
  .identity-title { font-size: 23px; color: var(--ink-gray); margin-top: 6px; }
  .address {
    position: absolute; left: 64px; top: 410px;
    font-size: 23px; font-style: normal; color: var(--ink-gray); line-height: 1.45;
  }
  .contact { position: absolute; left: 556px; top: 196px; }
  .contact-rule { position: absolute; left: 0; top: 0; }
  .contact-list { list-style: none; position: relative; margin-top: 50px; }
  .contact-item {
    display: flex; align-items: center; gap: 18px;
    height: 46px; font-size: 22px; color: var(--ink-gray); white-space: nowrap;
  }
  .contact-icon {
    width: 30px; height: 30px; border-radius: 6px;
    background: var(--icon-blue); flex: none;
    display: flex; align-items: center; justify-content: center;
  }
</style>
</head>
<body>
  <main class="card">
    <div class="brand">
      <span class="brand-square"></span>
      <span class="brand-name">Dorian T Welsby</span>
    </div>

    <div class="identity">
      <div class="identity-name">Dorian T Welsby</div>
      <div class="identity-title">Certified Public Accountant</div>
    </div>

    <address class="address">
      38-27 52nd Street<br>
      Sunnyside, NY 11287
    </address>

    <div class="contact">
      <svg class="contact-rule" width="30" height="300" viewBox="0 0 30 300" aria-hidden="true">
        <g fill="var(--dot-blue)">
          <circle cx="15" cy="4" r="2.4"/><circle cx="15" cy="16" r="2.4"/><circle cx="15" cy="28" r="2.4"/><circle cx="15" cy="40" r="2.4"/>
          <circle cx="15" cy="248" r="2.4"/><circle cx="15" cy="260" r="2.4"/><circle cx="15" cy="272" r="2.4"/><circle cx="15" cy="284" r="2.4"/>
        </g>
      </svg>
      <ul class="contact-list">
        <li class="contact-item">
          <span class="contact-icon">
            <svg width="18" height="18" viewBox="0 0 24 24" aria-label="Phone"><path fill="#fff" d="M6.6 10.8a15.1 15.1 0 0 0 6.6 6.6l2.2-2.2c.3-.3.7-.4 1-.2 1.1.4 2.3.6 3.6.6.6 0 1 .4 1 1V20c0 .6-.4 1-1 1A17 17 0 0 1 3 4c0-.6.4-1 1-1h3.5c.6 0 1 .4 1 1 0 1.3.2 2.5.6 3.6.1.3 0 .7-.2 1z"/></svg>
          </span>
          (718) 555-0142
        </li>
        <li class="contact-item">
          <span class="contact-icon">
            <svg width="18" height="18" viewBox="0 0 24 24" aria-label="Fax"><path fill="#fff" d="M7 3h10v5H7zM4 9h16a2 2 0 0 1 2 2v6h-4v4H6v-4H2v-6a2 2 0 0 1 2-2zm4 7v3h8v-3z"/></svg>
          </span>
          (888) 555-0199
        </li>
        <li class="contact-item">
          <span class="contact-icon">
            <svg width="18" height="18" viewBox="0 0 24 24" aria-label="Email"><path fill="#fff" d="M3 5h18v14H3zm2 2v.5l7 5 7-5V7zm0 3v7h14v-7l-7 5z"/></svg>
          </span>
          dtwthecpa@ledgerpost.com
        </li>
        <li class="contact-item">
          <span class="contact-icon">
            <svg width="18" height="18" viewBox="0 0 24 24" aria-label="Website"><circle cx="12" cy="12" r="9" fill="none" stroke="#fff" stroke-width="2"/><path d="M3 12h18M12 3c3 3 3 15 0 18M12 3c-3 3-3 15 0 18" fill="none" stroke="#fff" stroke-width="1.6"/></svg>
          </span>
          www.harborfilingreliefexperts.com
        </li>
      </ul>
    </div>
  </main>
</body>
</html>
```